Web design for Marketplace

Guys!
1st of all, thank you for willing to help me out.
I have attached PDF file with examples.
I am looking for professional and clean design for my new project “ Lantern of Seers “. Its marketplace for Psychic Readers around the world. Where they will able to register to provide their services via Chat,Email and sell their products on their personal stores.
Customer will able to get services and buy products from Psychic on Marketplace.
url : http://www.lanternofseers-demo.net
Please note: it doesn’t matter, what my current site looks like. I am looking for completely new design.
It doesn't matter if you add or remove : Clipvale video or even text which is on the home page in new design.
Following are the main pages of the website, which i am looking to be design.
1. Home page
2. Psychic
3. Marketplace
4. Psychic profile page
5. Psychic Store page
6. Psychic product page
7. Logo
following is the website, which i like the most. I would love to have something like that. It is neat , clean and friendly. I am looking for depth in design and neatness and borders (matter and a lot and it should be prefect ).
http://www.craftnook-demo.net
P.S : i believe it will be helpful to choose one of you. If you can only create design of " Homepage" at 1st , so i can go ahead and hire one of you guys.
Best,
Hi guys!
Guys,

```html
<!DOCTYPE html>
<html lang="en">
<head>
<meta charset="utf-8">
<title>Lantern of Seers – Home</title>
<link rel="stylesheet" href="https://fonts.googleapis.com/css2?family=Open+Sans:wght@400;600;700&family=Montserrat:wght@400;500;600&family=Lora:ital@1&display=swap">
<style>
:root{
  --blue:#1a8fcf;
  --blue-dark:#0f78b5;
  --text:#444;
  --muted:#888;
  --line:#e3e3e3;
  --green:#6fbf2a;
  --grey-dot:#d6d6d6;
  --orange:#f0591f;
  --sky:#bfe6f7;
  --page:#ffffff;
}
*{box-sizing:border-box;margin:0;padding:0}
html,body{width:1200px;height:2311px;overflow:hidden;background:var(--page)}
body{position:relative;font-family:"Open Sans",Arial,sans-serif;color:var(--text)}
.abs{position:absolute}
a{color:inherit;text-decoration:none}

/* header */
.brand{left:140px;top:24px;width:187px;height:72px;background:#fff;display:flex;align-items:center;gap:8px;padding-left:6px}
.brand-mark{width:14px;height:14px;background:var(--orange)}
.brand-name{font-family:"Montserrat",sans-serif;font-weight:600;font-size:21px;color:#222;line-height:1.05;width:150px}
.top-links{left:338px;top:16px;font-size:13px;color:var(--blue)}
.top-links a{margin-right:14px}
.help{left:1030px;top:16px;font-size:13px;color:var(--blue)}
.nav{left:337px;top:52px;width:722px;height:46px;background:linear-gradient(#f1f1f1,#dcdcdc);border:1px solid #cfcfcf;border-radius:3px;display:flex;align-items:center}
.nav a{font-size:14px;color:var(--blue);padding:0 15px;height:100%;display:flex;align-items:center;border-right:1px solid #c9c9c9}
.search{margin-left:auto;margin-right:10px;display:flex;gap:6px}
.search-field{width:322px;height:27px;background:#fff;border:1px solid #c4c4c4}
.search-btn{width:80px;height:27px;background:linear-gradient(#fafafa,#e2e2e2);border:1px solid #bdbdbd;border-radius:3px;font-size:13px;display:flex;align-items:center;justify-content:center;color:#444}

/* hero */
.hero{left:140px;top:123px;width:919px;height:362px;border-radius:4px;overflow:hidden;background:linear-gradient(135deg,#c9b7a5 0%,#e5e0da 30%,#b8a898 55%,#dcd6d0 80%,#a99584 100%)}
.hero-title{left:143px;top:141px;width:634px;height:83px;background:rgba(25,140,205,.93);border:3px solid rgba(255,255,255,.55);display:flex;align-items:center;justify-content:center;font-size:41px;font-weight:600;color:#fff;letter-spacing:-.3px}
.hero-band{left:0;bottom:0;width:100%;height:72px;background:rgba(20,20,20,.72);text-align:center;padding-top:6px}
.hero-band .lead{font-size:24px;color:#38b6ef;line-height:30px}
.hero-band .sub{font-size:19px;color:#fff;line-height:26px}

/* section heading */
.section-title{font-family:"Montserrat",sans-serif;font-weight:600;font-size:17px;color:var(--blue-dark);padding-bottom:10px;border-bottom:3px solid var(--blue)}
.rule{height:1px;background:var(--line)}

/* psychic cards */
.cards{left:140px;top:564px;width:919px;display:grid;grid-template-columns:repeat(3,288px);column-gap:27px;row-gap:26px}
.card{position:relative;height:239px;background:#fff;border:1px solid #e2e2e2;box-shadow:0 5px 6px -4px rgba(0,0,0,.25)}
.card-photo{position:absolute;left:15px;top:12px;width:80px;height:80px}
.card-name{position:absolute;left:105px;top:10px;font-family:"Montserrat",sans-serif;font-size:17px;font-weight:500;color:#333}
.card-role{position:absolute;left:105px;top:34px;font-size:10px;color:var(--muted)}
.card-price-label{position:absolute;left:105px;top:62px;font-size:12px;color:#555}
.card-price{position:absolute;left:105px;top:80px;font-size:13px;color:var(--blue)}
.status{position:absolute;right:15px;top:77px;font-size:12px;color:#aaa;display:flex;align-items:center;gap:5px}
.status::after{content:"";width:14px;height:14px;border-radius:50%;background:var(--grey-dot)}
.status.online{color:var(--green)}
.status.online::after{background:var(--green)}
.card-quote{position:absolute;left:15px;top:104px;width:258px;font-family:"Lora",Georgia,serif;font-style:italic;font-size:13px;line-height:19px;color:#9a9a9a;text-indent:20px}
.card-quote::before{content:"\201C";position:absolute;left:-20px;top:-6px;font-size:34px;color:#b5b5b5;text-indent:0}
.card-quote::after{content:"\201D";font-size:30px;color:#b5b5b5;vertical-align:-10px;margin-left:4px}
.read-more{position:absolute;right:16px;bottom:12px;font-size:12px;color:var(--blue)}

/* newsletter */
.newsletter{left:140px;top:1379px;width:191px;height:220px;background:#f3f3f3;border:1px solid #e5e5e5;padding:14px 13px}
.newsletter h3{font-family:"Montserrat",sans-serif;font-size:17px;font-weight:600;color:var(--blue-dark);margin-bottom:10px}
.newsletter p{font-size:13px;line-height:17px;color:#555;margin-bottom:10px}
.email-field{height:30px;border:1px solid #ccc;background:#fff;font-size:13px;padding:6px 8px;color:#333;margin-bottom:10px}
.signup-btn{width:87px;height:29px;border-radius:3px;background:linear-gradient(#4fc3f0,#1b9bd3);color:#fff;font-size:16px;font-weight:600;display:flex;align-items:center;justify-content:center;margin-bottom:10px}
.newsletter .more{font-size:12px;color:var(--blue)}

/* marketplace */
.market-head{left:364px;top:1380px;width:693px}
.market-grid{left:364px;top:1435px;width:693px;display:grid;grid-template-columns:repeat(8,73px);column-gap:14px;row-gap:17px}
.thumb{height:73px;border:1px solid #ddd}

/* join */
.join-shadow{left:130px;top:1690px;width:940px;height:16px;background:radial-gradient(ellipse at top,rgba(0,0,0,.12),rgba(0,0,0,0) 70%)}
.join{left:372px;top:1649px;width:456px;height:44px;display:flex;border-radius:4px;overflow:hidden;box-shadow:0 2px 3px rgba(0,0,0,.3)}
.join .ask{flex:0 0 286px;background:linear-gradient(#f57a3c,#e24b12);color:#fff;font-size:25px;font-weight:600;display:flex;align-items:center;justify-content:center}
.join .go{flex:1;background:linear-gradient(#555,#222);color:#fff;font-size:25px;font-weight:600;display:flex;align-items:center;justify-content:center}

/* video */
.video-frame{left:160px;top:1739px;width:404px;height:247px;background:#fff;border:1px solid #ddd;box-shadow:0 3px 8px rgba(0,0,0,.15);padding:16px}
.video-still{width:100%;height:100%;background:linear-gradient(160deg,#3a3a3a 0%,#6b5a4a 40%,#b59a7e 60%,#2b2b2b 100%)}
.video-brand{left:600px;top:1744px;display:flex;align-items:baseline;gap:12px}
.video-brand .name{font-family:"Open Sans",sans-serif;font-weight:700;font-size:34px;color:#222}
.video-brand .kind{font-size:27px;color:#444}
.video-title{left:600px;top:1814px;width:470px;font-size:28px;line-height:34px;font-weight:600;color:var(--blue)}
.video-text{left:600px;top:1900px;width:450px;font-size:15px;line-height:23px;color:#555}
.video-more{left:600px;top:1968px;font-size:12px;color:var(--blue)}

/* footer */
.footer-band{left:0;top:2042px;width:1200px;height:222px;background:linear-gradient(#8fd4f2 0%,var(--sky) 40%,#eaf7fd 100%)}
.map{left:140px;top:2071px;width:395px;height:163px;background:linear-gradient(135deg,#e7e4dd,#d9d6cf 60%,#ece9e2)}
.address{left:150px;top:2096px;width:212px;height:80px;background:#fff;border-radius:3px;box-shadow:0 1px 4px rgba(0,0,0,.3);padding:10px 14px;font-size:13px;line-height:18px;color:#333}
.address strong{font-weight:600;font-size:14px}
.pin{left:375px;top:2140px}
.contact-title{left:562px;top:2070px;font-family:"Montserrat",sans-serif;font-size:17px;font-weight:600;color:#222}
.contact-label{font-size:13px;color:#333}
.phone{left:562px;top:2125px}
.phone .num{font-size:25px;font-weight:600;color:var(--blue);line-height:34px}
.email{left:562px;top:2192px}
.email .addr{font-size:17px;font-weight:600;color:var(--blue);line-height:26px}
.social{left:869px;top:2182px}
.social .icons{display:flex;gap:6px;margin-top:6px}
.social .icons span{width:24px;height:24px;border-radius:50%;background:var(--blue)}
.footer-rule{left:140px;top:2264px;width:919px}
.footer-links{left:140px;top:2280px;font-size:11px;color:#444}
.footer-links a{margin-right:13px}
.copyright{left:662px;top:2280px;font-size:11px;color:#222}
</style>
</head>
<body>

<header>
  <div class="abs brand"><span class="brand-mark"></span><span class="brand-name">Lantern of Seers</span></div>
  <div class="abs top-links"><a href="#">Login</a><a href="#">Signup</a></div>
  <a class="abs help" href="#">Help</a>
  <nav class="abs nav">
    <a href="#">Psychic</a><a href="#">Marketplace</a><a href="#">My account</a>
    <div class="search"><div class="search-field"></div><div class="search-btn">Search</div></div>
  </nav>
</header>

<section class="abs hero" role="img" aria-label="Photo collage of many smiling people holding up white frames">
  <div class="abs hero-title">Meet Our Expert Lantern Seers</div>
  <div class="abs hero-band">
    <div class="lead">The best psychics are here for you try a live psychic reading today.</div>
    <div class="sub">A live psychic reading is your chance to ask questions, get answers.</div>
  </div>
</section>

<div class="abs" style="left:140px;top:507px;width:919px">
  <div class="rule" style="position:absolute;left:0;right:0;top:34px"></div>
  <span class="section-title" style="display:inline-block;position:relative">Top Pyschics</span>
</div>

<section class="abs cards">
  <article class="card">
    <div class="card-photo" role="img" aria-label="Portrait of psychic" style="background:linear-gradient(#5a4a3e,#8c7563)"></div>
    <div class="card-name">Dario Fenwick</div><div class="card-role">Product Owner, Kestrel Works</div>
    <div class="card-price-label">Price</div><div class="card-price">$ 1.99 / min</div>
    <div class="status">Offline</div>
    <p class="card-quote">Lorem Ipsum. Proin gravida nibh vel velit auctor aliquet. Aenean sollicitudin, lorem quis bibendum auctor, nisi elit consequat ipsum, nec sagittis sem nibh id elit.</p>
    <a class="read-more" href="#">Read more</a>
  </article>
  <article class="card">
    <div class="card-photo" role="img" aria-label="Portrait of psychic" style="background:linear-gradient(#d8d2cc,#9c8470)"></div>
    <div class="card-name">Ross Lindqvist</div><div class="card-role">CEO and Founder</div>
    <div class="card-price-label">Price</div><div class="card-price">$ 3.99 / min</div>
    <div class="status">Offline</div>
    <p class="card-quote">Lorem Ipsum. Proin gravida nibh vel velit auctor aliquet. Aenean sollicitudin, lorem quis bibendum auctor, nisi elit consequat ipsum, nec sagittis sem nibh id elit.</p>
    <a class="read-more" href="#">Read more</a>
  </article>
  <article class="card">
    <div class="card-photo" role="img" aria-label="Portrait of psychic" style="background:linear-gradient(#c96a2c,#8a5036)"></div>
    <div class="card-name">Milan</div><div class="card-role">Product Owner, Kestrel Works</div>
    <div class="card-price-label">Price</div><div class="card-price">$ 2.99 / min</div>
    <div class="status online">Online</div>
    <p class="card-quote">Lorem Ipsum. Proin gravida nibh vel velit auctor aliquet. Aenean sollicitudin, lorem quis bibendum auctor, nisi elit consequat ipsum, nec sagittis sem nibh id elit.</p>
    <a class="read-more" href="#">Read more</a>
  </article>
  <article class="card">
    <div class="card-photo" role="img" aria-label="Portrait of psychic" style="background:linear-gradient(#e9e4de,#c9a98a)"></div>
    <div class="card-name">Lorem Ipsum</div><div class="card-role">Product Owner, Kestrel Works</div>
    <div class="card-price-label">Price</div><div class="card-price">$ 4.99 / min</div>
    <div class="status online">Online</div>
    <p class="card-quote">Lorem Ipsum. Proin gravida nibh vel velit auctor aliquet. Aenean sollicitudin, lorem quis bibendum auctor, nisi elit consequat ipsum, nec sagittis sem nibh id elit.</p>
    <a class="read-more" href="#">Read more</a>
  </article>
  <article class="card">
    <div class="card-photo" role="img" aria-label="Portrait of psychic" style="background:linear-gradient(#2a1f1c,#b07d68)"></div>
    <div class="card-name">Lorem Ipsum</div><div class="card-role">Product Owner, Kestrel Works</div>
    <div class="card-price-label">Price</div><div class="card-price">$ 5.00 / min</div>
    <div class="status">Offline</div>
    <p class="card-quote">Lorem Ipsum. Proin gravida nibh vel velit auctor aliquet. Aenean sollicitudin, lorem quis bibendum auctor, nisi elit consequat ipsum, nec sagittis sem nibh id elit.</p>
    <a class="read-more" href="#">Read more</a>
  </article>
  <article class="card">
    <div class="card-photo" role="img" aria-label="Portrait of psychic" style="background:linear-gradient(#e4e0dc,#8f6f58)"></div>
    <div class="card-name">Lorem Ipsum</div><div class="card-role">Product Owner, Kestrel Works</div>
    <div class="card-price-label">Price</div><div class="card-price">$ 3.00 / min</div>
    <div class="status">Offline</div>
    <p class="card-quote">Lorem Ipsum. Proin gravida nibh vel velit auctor aliquet. Aenean sollicitudin, lorem quis bibendum auctor, nisi elit consequat ipsum, nec sagittis sem nibh id elit.</p>
    <a class="read-more" href="#">Read more</a>
  </article>
  <article class="card">
    <div class="card-photo" role="img" aria-label="Portrait of psychic" style="background:linear-gradient(#6a6a6a,#b08e77)"></div>
    <div class="card-name">Lorem Ipsum</div><div class="card-role">Product Owner, Kestrel Works</div>
    <div class="card-price-label">Price</div><div class="card-price">$ 4.00 / min</div>
    <div class="status">Offline</div>
    <p class="card-quote">Lorem Ipsum. Proin gravida nibh vel velit auctor aliquet. Aenean sollicitudin, lorem quis bibendum auctor, nisi elit consequat ipsum, nec sagittis sem nibh id elit.</p>
    <a class="read-more" href="#">Read more</a>
  </article>
  <article class="card">
    <div class="card-photo" role="img" aria-label="Portrait of psychic" style="background:linear-gradient(#8c3a22,#c89a84)"></div>
    <div class="card-name">Lorem Ipsum</div><div class="card-role">Product Owner, Kestrel Works</div>
    <div class="card-price-label">Price</div><div class="card-price">$ 3.50 / min</div>
    <div class="status online">Online</div>
    <p class="card-quote">Lorem Ipsum. Proin gravida nibh vel velit auctor aliquet. Aenean sollicitudin, lorem quis bibendum auctor, nisi elit consequat ipsum, nec sagittis sem nibh id elit.</p>
    <a class="read-more" href="#">Read more</a>
  </article>
  <article class="card">
    <div class="card-photo" role="img" aria-label="Portrait of psychic" style="background:linear-gradient(#f2eeea,#5a3a2a)"></div>
    <div class="card-name">Lorem Ipsum</div><div class="card-role">Product Owner, Kestrel Works</div>
    <div class="card-price-label">Price</div><div class="card-price">$ 2.00 / min</div>
    <div class="status">Offline</div>
    <p class="card-quote">Lorem Ipsum. Proin gravida nibh vel velit auctor aliquet. Aenean sollicitudin, lorem quis bibendum auctor, nisi elit consequat ipsum, nec sagittis sem nibh id elit.</p>
    <a class="read-more" href="#">Read more</a>
  </article>
</section>

<aside class="abs newsletter">
  <h3>Daily Finds Email</h3>
  <p>Get gift ideas, editors' picks &amp; fresh trends in your inbox.</p>
  <div class="email-field">Enter your email</div>
  <div class="signup-btn">Sign Up</div>
  <a class="more" href="#">See our other newsletters</a>
</aside>

<div class="abs market-head">
  <div class="rule" style="position:absolute;left:0;right:0;top:33px"></div>
  <span class="section-title" style="display:inline-block;position:relative">Psychic Marketplace</span>
</div>
<section class="abs market-grid">
  <div class="thumb" role="img" aria-label="Product photo: turquoise beads" style="background:linear-gradient(135deg,#8fd8dc,#4fb8c2)"></div>
  <div class="thumb" role="img" aria-label="Product photo: beaded bracelet" style="background:linear-gradient(135deg,#6a4a36,#2fa3b0)"></div>
  <div class="thumb" role="img" aria-label="Product photo: pink beads" style="background:linear-gradient(135deg,#e9b7d6,#b77fb0)"></div>
  <div class="thumb" role="img" aria-label="Product photo: colourful glass beads" style="background:linear-gradient(135deg,#d45aa8,#7ab6d9)"></div>
  <div class="thumb" role="img" aria-label="Product photo: blue glass pendants" style="background:linear-gradient(135deg,#c9d3e0,#3f6aa8)"></div>
  <div class="thumb" role="img" aria-label="Product photo: silver bead charm" style="background:linear-gradient(135deg,#9aa2a8,#4b6c8f)"></div>
  <div class="thumb" role="img" aria-label="Product photo: teal pendant" style="background:linear-gradient(135deg,#4a5a5a,#2fa0a8)"></div>
  <div class="thumb" role="img" aria-label="Product photo: vintage cufflinks" style="background:linear-gradient(135deg,#8a6a50,#c9b59a)"></div>
  <div class="thumb" role="img" aria-label="Product photo: blue bead charm" style="background:linear-gradient(135deg,#a9b3bd,#2f5f8f)"></div>
  <div class="thumb" role="img" aria-label="Product photo: blue glass drops" style="background:linear-gradient(135deg,#dfe6ee,#3e6fc0)"></div>
  <div class="thumb" role="img" aria-label="Product photo: turquoise bracelet" style="background:linear-gradient(135deg,#3a2a22,#2fa3b0)"></div>
  <div class="thumb" role="img" aria-label="Product photo: silver cufflinks" style="background:linear-gradient(135deg,#8a7560,#d4cbbd)"></div>
  <div class="thumb" role="img" aria-label="Product photo: turquoise beads" style="background:linear-gradient(135deg,#a5e0e4,#5bc0c8)"></div>
  <div class="thumb" role="img" aria-label="Product photo: beaded bracelet" style="background:linear-gradient(135deg,#3b2a22,#2fa3b0)"></div>
  <div class="thumb" role="img" aria-label="Product photo: colourful glass beads" style="background:linear-gradient(135deg,#d45aa8,#e6b84a)"></div>
  <div class="thumb" role="img" aria-label="Product photo: pink beads" style="background:linear-gradient(135deg,#f0c4de,#c88fc0)"></div>
</section>

<div class="abs join-shadow"></div>
<a class="abs join" href="#"><span class="ask">Are you PSYCHIC?</span><span class="go">Join Now</span></a>

<section>
  <div class="abs video-frame"><div class="video-still" role="img" aria-label="Video still of a woman speaking to camera in a room"></div></div>
  <div class="abs video-brand"><span class="name">Clipvale</span><span class="kind">Video</span></div>
  <h2 class="abs video-title">How to be psychic, have intuition, and do mind reading</h2>
  <p class="abs video-text">Lorem Ipsum Proin gravida nibh vel velit auctor aliquet. Aenean sollicitudin, lorem quis bibendum auctor, nisi elit consequat ipsum, nec sagittis sem nibh id elit.</p>
  <a class="abs video-more" href="#">Read more »</a>
</section>

<footer>
  <div class="abs footer-band"></div>
  <div class="abs map" role="img" aria-label="Street map around the office location"></div>
  <div class="abs address"><strong>Lantern of Seers</strong><br>72 Orchard Row<br>lorem quis, NJ 000000</div>
  <svg class="abs pin" width="22" height="30" viewBox="0 0 22 30" aria-hidden="true"><path d="M11 1C5.5 1 1 5.4 1 10.8 1 18 11 29 11 29s10-11 10-18.2C21 5.4 16.5 1 11 1z" fill="#6fbf2a" stroke="#3f7f18"/><circle cx="11" cy="10.5" r="3.5" fill="#fff"/></svg>
  <div class="abs contact-title">Get In Touch</div>
  <div class="abs phone"><div class="contact-label">Give us a call at</div><div class="num">(+ 1) 555-010-2468</div></div>
  <div class="abs email"><div class="contact-label">Email us at</div><div class="addr">info@lanternofseers-demo.net</div></div>
  <div class="abs social"><div class="contact-label">Connect with us</div><div class="icons"><span></span><span></span></div></div>
  <div class="abs rule footer-rule"></div>
  <nav class="abs footer-links"><a href="#">About Us</a><a href="#">About Psychic Readings</a><a href="#">Contact Us</a><a href="#">Privacy Policy</a><a href="#">Terms &amp; Conditions</a></nav>
  <div class="abs copyright">© 2013 Lantern of Seers (ACN 000 111 222). Trademark Lantern of Seers</div>
</footer>

</body>
</html>
```